BRINDLEMARK STUDIOS PRODUCT CATALOG

Rustic and Elegant Boutique Custom and personalized furniture and Kitchen accessories with a contemporary art Flair. My product is very personable. I put an effort into everyone like it is my own. From Western red cedar toWestern red cedar to Eastern giant Bonzai. Are use word from all over the world. Including,Eastern Mauyi Bonzai. I use wood from all over the world. And can do custom orders for Desired . I make style tables that include varnish is on some of the more beautiful pieces of wood natural and some of the others I turn into river tables or waterfall tables. This involves a lot of coloured Apoxsee and many hours ofI make style tables that include varnish is on some of the more beautiful pieces of wood natural and some of the others I turn into river tables or waterfall tables. This involves a lot of epoxy and many hours of work mixing colours or sanding down the curve to the perfect circumference at the end of the day each one is a piece of art in itself generally 56 feet and legsmixing colours or sanding down the curve to the perfect circumference at the end of the day each one is a piece of art in itself. In my practice I also use a lot of original woodworking tools from the 30s and 40s. Not allIn my practice I also use a lot of original woodworking tools from the 30s to 70s. I also produce in tables hallway tables sofa tables boardroom tables and all actuality I can make any table you want it'll just be one of a kind. A cut above, like none other.

Target Market(s)

The elite. Higher and then a class above. Affluent Female home owners. High end interior designers. Exclusive corporate gifts and furnishings .

Industry/Entity Type

Home Furnishing

Font styles to use
Other font styles liked:
• See attached branding board.

Requirements
Must have
• My logo Black & Gold big on cover subtly next to page #'s on outside corners on every page. Matte Cover page then glossy inside catalog. Source file included. One product per page for larger pieces. Along with multiple small pieces per page. Leave room for write up for each pice.
Must convey sophisticated yet down to earth. Emphasis on each pieces uniqueness and story. Use colours from attached branding board.
Nice to have
• Having the smaller pieces on pages formatted vertically along side of pages.
Should not have
• Avoid looking too over bearing or flashy.

```html
<!DOCTYPE html>
<html lang="en">
<head>
<meta charset="utf-8">
<title>Brindlemark Studios – Catalog Cover</title>
<link rel="stylesheet" href="https://fonts.googleapis.com/css2?family=Alfa+Slab+One&family=Noto+Serif:wght@700&display=swap">
<style>
  :root {
    --backdrop: #5b5957;
    --paper: #f6f6f6;
    --orange: #e9641f;
    --orange-deep: #e3511a;
    --charcoal: #3a3836;
    --ink: #1f1f1f;
    --photo-light: #dfe4e8;
    --photo-mid: #b9c0c5;
    --wood: #d98a2c;
  }
  html, body {
    margin: 0;
    width: 1200px;
    height: 840px;
    overflow: hidden;
    background: var(--backdrop);
  }
  .canvas {
    position: relative;
    width: 1200px;
    height: 840px;
  }
  .cover {
    position: absolute;
    left: 300px;
    top: 30px;
    width: 600px;
    height: 780px;
    background: var(--paper);
    box-shadow: 0 10px 30px rgba(0,0,0,0.35);
    overflow: hidden;
  }
  .cover svg { display: block; }
  .brand-title {
    font-family: "Alfa Slab One", serif;
    font-size: 44px;
    fill: var(--orange);
  }
  .tagline {
    font-family: "Noto Serif", serif;
    font-weight: 700;
    font-size: 17px;
    letter-spacing: 1.2px;
    fill: var(--ink);
  }
  .web-address {
    font-family: "Noto Serif", serif;
    font-weight: 700;
    font-size: 21px;
    letter-spacing: 1px;
    fill: #ffffff;
  }
</style>
</head>
<body>
<div class="canvas">
  <div class="cover">
    <svg width="600" height="780" viewBox="0 0 600 780" xmlns="http://www.w3.org/2000/svg">
      <defs>
        <linearGradient id="orangeFill" x1="0" y1="0" x2="0" y2="1">
          <stop offset="0" stop-color="var(--orange)"/>
          <stop offset="1" stop-color="var(--orange-deep)"/>
        </linearGradient>
        <radialGradient id="tablePhotoTop" cx="0.5" cy="0.45" r="0.6">
          <stop offset="0" stop-color="var(--photo-light)"/>
          <stop offset="0.6" stop-color="var(--photo-mid)"/>
          <stop offset="1" stop-color="#c9a06a"/>
        </radialGradient>
        <radialGradient id="tablePhotoBottom" cx="0.5" cy="0.5" r="0.6">
          <stop offset="0" stop-color="var(--wood)"/>
          <stop offset="0.55" stop-color="#e7c79a"/>
          <stop offset="1" stop-color="var(--photo-light)"/>
        </radialGradient>
      </defs>

      <!-- charcoal swoosh edge -->
      <path class="swoosh-edge" fill="var(--charcoal)" transform="translate(22,12)"
        d="M0,0 H565 C660,90 640,320 470,345 C390,357 330,245 200,240 C90,236 30,310 40,395 C50,500 130,560 230,580 C320,600 370,680 390,780 H0 Z"/>

      <!-- orange field -->
      <path class="orange-field" fill="url(#orangeFill)"
        d="M0,0 H565 C660,90 640,320 470,345 C390,357 330,245 200,240 C90,236 30,310 40,395 C50,500 130,560 230,580 C320,600 370,680 390,780 H0 Z"/>

      <!-- featured product circles -->
      <g class="feature-photo feature-photo--top">
        <circle cx="430" cy="175" r="128" fill="none" stroke="#ffffff" stroke-width="5"/>
        <circle cx="430" cy="175" r="119" fill="url(#tablePhotoTop)"
          role="img" aria-label="Photo of a live-edge wooden bench with a green epoxy river on steel legs"/>
      </g>
      <g class="feature-photo feature-photo--bottom">
        <circle cx="185" cy="400" r="118" fill="#ffffff" stroke="var(--orange)" stroke-width="3"/>
        <circle cx="185" cy="400" r="111" fill="url(#tablePhotoBottom)"
          role="img" aria-label="Photo of a glossy amber wooden table on hairpin legs"/>
      </g>

      <!-- brand block -->
      <text class="brand-title" x="190" y="565" textLength="395" lengthAdjust="spacingAndGlyphs">Brindlemark Studios</text>
      <text class="tagline" x="400" y="598" text-anchor="middle">Rustic and Elegant wooden</text>
      <text class="tagline" x="400" y="622" text-anchor="middle">furniture &amp; Kitchen accessories</text>

      <!-- web band -->
      <rect class="web-band" x="255" y="655" width="345" height="42" fill="var(--orange)"/>
      <text class="web-address" x="428" y="684" text-anchor="middle">www.brindlemarkstudios.com</text>
    </svg>
  </div>
</div>
</body>
</html>
```